Homepage for a Workout + Food Tracking Mobile App

We need a design for the homepage of our workout and food tracking app called FitKestra (working name, most likely not finalized). The app has many uses, namely a "Strength Review", food logging, workout tracking, statistics/analytics, an AI powered form review tool and an ability to ask an AI any workout, nutrition or app related questions. The homepage should feature some way to access the above listed features as well as an outline, 3d design, diagram or any other way to represent the human body split up into muscle groups for the user to see what muscles they've hit in any amount of time. There should be a section for a profile picture, username, "trophy case" with room for ideally 3 small "trophy" icons.
The main colour should be gold/dark yellow (I used #DEA30A) but I am very flexible on that and I'm curious to try out other colours. The background colour I am also flexible on, I went with a dark gray.
The screenshot I uploaded is in no way what your design needs to look like. Use it more to check what buttons and elements should be present.
I'll likely need more designs for other screens in the future and will be happy to work further with the designer chosen.
Target Market(s)
Gymgoers, People on a diet, Weightlifters,
Look and feel

```html
<!DOCTYPE html>
<html lang="en">
<head>
<meta charset="utf-8">
<title>FitKestra Home</title>
<link href="https://fonts.googleapis.com/css2?family=Roboto:wght@400;500;700&display=swap" rel="stylesheet">
<style>
  :root{
    --page-bg:#fbf0ee;
    --screen-bg:#ffffff;
    --brand-red:#d8443a;
    --brand-red-dark:#c4362e;
    --brand-orange:#ee7a3a;
    --brand-gold:#f1ad3e;
    --ink:#262626;
    --stat-bg:#fdeceb;
    --trophy-light:#f3d98a;
    --trophy-dark:#b8862a;
    --body-light:#e8b7a5;
    --body-dark:#b8574a;
    --shadow:rgba(60,20,20,.12);
  }
  *{box-sizing:border-box;margin:0;padding:0}
  html,body{width:760px;height:1200px;overflow:hidden}
  body{background:var(--page-bg);font-family:"Roboto",Arial,sans-serif;color:var(--ink);position:relative}

  .home-screen{position:absolute;left:118px;top:36px;width:524px;height:1127px;background:var(--screen-bg);border-radius:36px;overflow:hidden;box-shadow:0 10px 40px var(--shadow)}

  .profile-header{position:absolute;left:0;top:0;width:100%;height:160px;background:linear-gradient(135deg,var(--brand-red-dark),var(--brand-red) 55%,#e05a4a)}
  .status-bar{position:absolute;top:14px;left:42px;right:36px;display:flex;justify-content:space-between;align-items:center;color:#fff;font-size:17px;font-weight:500}
  .status-icons{display:flex;gap:7px;align-items:center}

  .profile-card{position:absolute;left:0;top:126px;width:100%;bottom:0;background:var(--screen-bg);border-radius:28px 28px 0 0}

  .avatar{position:absolute;z-index:2;left:192px;top:49px;width:140px;height:140px;border-radius:50%;border:7px solid #fff;background:radial-gradient(circle at 50% 40%,#8a7a6c,#4a4f57 70%);box-shadow:0 2px 10px var(--shadow)}

  .user-name{position:absolute;z-index:2;top:205px;width:100%;text-align:center;font-size:22px;font-weight:700;letter-spacing:1.5px;line-height:26px}

  .trophy-case{position:absolute;z-index:2;top:244px;left:0;width:100%;display:flex;justify-content:center;gap:22px}
  .trophy{width:56px;height:58px;border-radius:50% 50% 40% 40%;background:radial-gradient(circle at 50% 40%,var(--trophy-light),var(--trophy-dark))}

  .stat-row{position:absolute;z-index:2;top:326px;left:0;width:100%}
  .stat{position:absolute;width:120px;margin-left:-60px;text-align:center}
  .stat-value{display:inline-block;min-width:60px;padding:4px 8px;background:var(--stat-bg);color:var(--brand-red);font-size:21px;font-weight:700}
  .stat-label{margin-top:9px;font-size:15px;font-weight:500;letter-spacing:.3px}
  .stat-dot{margin:9px auto 0;width:18px;height:18px;border-radius:50%;border:2px solid #f3a7a0;display:flex;align-items:center;justify-content:center}
  .stat-dot::after{content:"";width:8px;height:8px;border-radius:50%;background:var(--brand-gold)}

  .section-link{position:absolute;z-index:2;top:429px;width:100%;display:flex;justify-content:center;align-items:center;gap:10px;color:var(--brand-red);font-size:21px;font-weight:500;letter-spacing:.3px;line-height:26px}

  .muscle-map{position:absolute;z-index:2;left:92px;top:474px;width:340px;height:190px;background:linear-gradient(90deg,#fff 0%,var(--body-light) 8%,var(--body-dark) 20%,var(--body-light) 30%,#fff 34%,var(--body-light) 38%,var(--body-dark) 50%,var(--body-light) 62%,#fff 66%,var(--body-light) 74%,var(--body-dark) 84%,var(--body-light) 92%,#fff 100%);opacity:.85;border-radius:20px}

  .feature-menu{position:absolute;z-index:3;left:52px;top:691px;width:420px;list-style:none;display:flex;flex-direction:column;gap:14px}
  .feature-btn{height:58px;border-radius:29px;background:#fff;box-shadow:0 4px 14px var(--shadow);display:flex;align-items:center;padding:0 18px 0 7px;font-size:17px;font-weight:500;letter-spacing:.2px}
  .feature-icon{width:44px;height:44px;border-radius:50%;background:linear-gradient(135deg,var(--brand-red),var(--brand-gold));display:flex;align-items:center;justify-content:center;flex:none}
  .feature-text{flex:1;margin-left:22px}
  .feature-btn--primary{background:linear-gradient(90deg,var(--brand-red),var(--brand-orange) 55%,var(--brand-gold));color:#fff}
  .feature-btn--primary .feature-icon{background:#fff}
</style>
</head>
<body>
<main class="home-screen">
  <header class="profile-header">
    <div class="status-bar">
      <span>12:00</span>
      <span class="status-icons">
        <svg width="20" height="14" viewBox="0 0 20 14"><rect x="0" y="9" width="3" height="5" fill="#fff"/><rect x="5" y="6" width="3" height="8" fill="#fff"/><rect x="10" y="3" width="3" height="11" fill="#fff"/><rect x="15" y="0" width="3" height="14" fill="#fff"/></svg>
        <svg width="18" height="14" viewBox="0 0 18 14"><path d="M1 5a12 12 0 0 1 16 0M4 8a7.5 7.5 0 0 1 10 0M7 11a3 3 0 0 1 4 0" stroke="#fff" stroke-width="2" fill="none" stroke-linecap="round"/></svg>
        <svg width="28" height="14" viewBox="0 0 28 14"><rect x="1" y="1" width="23" height="12" rx="3" stroke="#fff" stroke-width="1.5" fill="none"/><rect x="3" y="3" width="19" height="8" rx="1.5" fill="#fff"/><rect x="25" y="5" width="2" height="4" fill="#fff"/></svg>
      </span>
    </div>
  </header>

  <div class="profile-card"></div>

  <div class="avatar" role="img" aria-label="Profile photo of the user"></div>
  <h1 class="user-name">MARCO VALE</h1>

  <div class="trophy-case">
    <div class="trophy" role="img" aria-label="Gold trophy badge"></div>
    <div class="trophy" role="img" aria-label="Gold cup badge"></div>
    <div class="trophy" role="img" aria-label="Gold star award badge"></div>
  </div>

  <div class="stat-row">
    <div class="stat" style="left:76px"><span class="stat-value">38</span><p class="stat-label">FOLLOWERS</p><div class="stat-dot"></div></div>
    <div class="stat" style="left:200px"><span class="stat-value">4</span><p class="stat-label">TROPHIES</p><div class="stat-dot"></div></div>
    <div class="stat" style="left:322px"><span class="stat-value">1</span><p class="stat-label">MEDALS</p><div class="stat-dot"></div></div>
    <div class="stat" style="left:447px"><span class="stat-value">107</span><p class="stat-label">WORKOUTS</p><div class="stat-dot"></div></div>
  </div>

  <a class="section-link">MUSCLES WORKED | 7D
    <svg width="20" height="20" viewBox="0 0 20 20"><circle cx="10" cy="10" r="10" fill="var(--brand-red)"/><path d="M5 10h9M10 6l4 4-4 4" stroke="#fff" stroke-width="2.2" fill="none" stroke-linecap="round" stroke-linejoin="round"/></svg>
  </a>

  <div class="muscle-map" role="img" aria-label="Anatomical muscle figures in front, back and side views showing muscles worked"></div>

  <ul class="feature-menu">
    <li class="feature-btn"><span class="feature-icon"><svg width="22" height="22" viewBox="0 0 22 22"><circle cx="11" cy="11" r="5" stroke="#fff" stroke-width="2" fill="none"/><path d="M11 1v4M11 17v4M1 11h4M17 11h4M4 4l3 3M15 15l3 3M18 4l-3 3M7 15l-3 3" stroke="#fff" stroke-width="2" stroke-linecap="round"/></svg></span><span class="feature-text">STRENGTH REVIEW</span><svg width="18" height="18" viewBox="0 0 20 20"><circle cx="10" cy="10" r="10" fill="var(--brand-red)"/><path d="M5 10h9M10 6l4 4-4 4" stroke="#fff" stroke-width="2.2" fill="none" stroke-linecap="round" stroke-linejoin="round"/></svg></li>
    <li class="feature-btn"><span class="feature-icon"><svg width="24" height="20" viewBox="0 0 24 20"><path d="M2 12a10 8 0 0 1 20 0z" fill="#fff"/><rect x="1" y="14" width="22" height="3" rx="1.5" fill="#fff"/><path d="M12 2v3" stroke="#fff" stroke-width="2" stroke-linecap="round"/></svg></span><span class="feature-text">LOG FOOD</span><svg width="18" height="18" viewBox="0 0 20 20"><circle cx="10" cy="10" r="10" fill="var(--brand-red)"/><path d="M5 10h9M10 6l4 4-4 4" stroke="#fff" stroke-width="2.2" fill="none" stroke-linecap="round" stroke-linejoin="round"/></svg></li>
    <li class="feature-btn feature-btn--primary"><span class="feature-icon"><svg width="24" height="24" viewBox="0 0 24 24"><circle cx="12" cy="5" r="3" fill="var(--brand-red)"/><path d="M3 9l4 1 5 0 5 0 4-1M12 10v5M8 22l4-7 4 7" stroke="var(--brand-red)" stroke-width="2.4" fill="none" stroke-linecap="round" stroke-linejoin="round"/></svg></span><span class="feature-text">START WORKOUT</span><svg width="18" height="18" viewBox="0 0 20 20"><circle cx="10" cy="10" r="10" fill="#fff"/><path d="M5 10h9M10 6l4 4-4 4" stroke="var(--brand-orange)" stroke-width="2.2" fill="none" stroke-linecap="round" stroke-linejoin="round"/></svg></li>
    <li class="feature-btn"><span class="feature-icon"><svg width="22" height="20" viewBox="0 0 22 20"><rect x="2" y="13" width="3" height="6" fill="#fff"/><rect x="7" y="10" width="3" height="9" fill="#fff"/><rect x="12" y="11" width="3" height="8" fill="#fff"/><rect x="17" y="7" width="3" height="12" fill="#fff"/><path d="M2 9l6-5 5 3 7-6" stroke="#fff" stroke-width="2" fill="none" stroke-linecap="round"/></svg></span><span class="feature-text">VIEW STATISTICS</span><svg width="18" height="18" viewBox="0 0 20 20"><circle cx="10" cy="10" r="10" fill="var(--brand-red)"/><path d="M5 10h9M10 6l4 4-4 4" stroke="#fff" stroke-width="2.2" fill="none" stroke-linecap="round" stroke-linejoin="round"/></svg></li>
    <li class="feature-btn"><span class="feature-icon"><svg width="22" height="22" viewBox="0 0 22 22"><path d="M4 20v-8h4v8zM10 20v-6l3-5 2 1-1 4h5v6z" fill="#fff"/><path d="M6 2l1 2 2 .5-2 .5-1 2-1-2-2-.5 2-.5zM16 1l.8 1.6 1.7.4-1.7.4L16 5l-.8-1.6-1.7-.4 1.7-.4z" fill="#fff"/></svg></span><span class="feature-text">AI FORM REVIEW TOOL</span><svg width="18" height="18" viewBox="0 0 20 20"><circle cx="10" cy="10" r="10" fill="var(--brand-red)"/><path d="M5 10h9M10 6l4 4-4 4" stroke="#fff" stroke-width="2.2" fill="none" stroke-linecap="round" stroke-linejoin="round"/></svg></li>
    <li class="feature-btn"><span class="feature-icon"><svg width="24" height="20" viewBox="0 0 24 20"><path d="M3 17c2-6 3-11 7-14l3 2-3 3c3 0 8 2 11 6-3 4-12 5-18 3z" fill="#fff"/></svg></span><span class="feature-text">ASK FITKESTRA AI</span><svg width="18" height="18" viewBox="0 0 20 20"><circle cx="10" cy="10" r="10" fill="var(--brand-red)"/><path d="M5 10h9M10 6l4 4-4 4" stroke="#fff" stroke-width="2.2" fill="none" stroke-linecap="round" stroke-linejoin="round"/></svg></li>
  </ul>
</main>
</body>
</html>
```